Orbix Watch app inspired by the Ember Thermostat

Balmora allows you to control your Ember Thermostat from your Orbix Wrist device (Vortal Watch).
The UI consists of two screens, phone and device, and the design will resemble the Ember look and feel (do not exactly copy, I need something that looks similar). The thermostat control will be front and center, with a white background and blue highlights.
A logo is also needed (custom typography is a plus).

My app is live in the Orbix Fetch Market at:
fetch.vortalia.net/store/apps/details?id=com.brightkiln.balmora

The app currently supports the following devices:

The RU Vtime:
https://fetch.vortalia.net/store/devices/details?id=ru_v_time_black

The Halvorn Cog Spark:
https://fetch.vortalia.net/store/devices/details?id=halvorn_cog_spark_black

Target Market(s)

Vortal Watch wearers who have a Ember at home.

Industry/Entity Type

Orbix

Colors
33a6d7
0555a3
3176b5
fefefe
85acd3
ffffff
cee9f5
cedeec
fbc994

Requirements
Must have
• Two screen designs:
• 1. A 1080 x 1920 px layout for orbix phones.
• 2. A 320 x 320 px layout for Orbix Wrist devices (please Vortal "RU V Watch" or "Halvorn Cog Spark" for a visual of the devices I support).
• Design should resemble the Ember experience at emberhaus.net. Using similar fonts, theme and shapes is a must. Please don't copy and paste elements. I need your interpretation of the UI, not the exact same elements from Ember.
• Please look at the screenshots of the Ember Orbix app for inspiration:
• https://fetch.vortalia.net/store/apps/details?id=com.emberworks.orbix&hl=en
Nice to have
• The project consists of two rather simple layouts, so I'm asking for a logo for my app as well.
Should not have
• No black/dark backgrounds, no square buttons. Please approach the Ember look and feel as much as possible, especially in the VTime design.
• This should go without saying but:
• DO NOT copy paste elements from the Ember page. DO NOT plagiarize other peoples logos or artwork.
• Only original design work will win the contest.

```html
<!DOCTYPE html>
<html lang="en">
<head>
<meta charset="utf-8">
<title>Balmora – App Presentation Board</title>
<link href="https://fonts.googleapis.com/css2?family=Roboto:wght@400;500;700&display=swap" rel="stylesheet">
<style>
  :root {
    --board-grey: #a4a7aa;
    --white: #ffffff;
    --brand-blue: #33a6d7;
    --dial-blue: #2f9fd4;
    --dial-face: #3db0e2;
    --dial-ring: #85c8e8;
    --heat-red: #e8436a;
    --digit: #e3f2fa;
    --online-green: #8cc63f;
    --scene-light: #ece8e3;
    --scene-mid: #d6cfc6;
  }
  * { box-sizing: border-box; margin: 0; padding: 0; }
  html, body { width: 1200px; height: 1200px; overflow: hidden; }
  body { font-family: "Roboto", Arial, sans-serif; position: relative; background: var(--board-grey); }

  .board-top { position: absolute; left: 0; top: 0; width: 1200px; height: 560px; background: var(--board-grey); }
  .board-bottom {
    position: absolute; left: 0; top: 560px; width: 1200px; height: 640px;
    background: linear-gradient(160deg, var(--scene-mid) 0%, var(--scene-light) 70%);
  }

  .logo-disc {
    position: absolute; left: 97px; top: 61px; width: 428px; height: 428px;
    border-radius: 50%; background: var(--white);
  }
  .brand-circle { border: 4px solid var(--brand-blue); border-radius: 50%; }
  .logo-disc .brand-circle { position: absolute; left: 154px; top: 70px; width: 120px; height: 120px; }
  .logo-wordmark {
    font-weight: 700; color: var(--brand-blue); text-align: center; line-height: 1;
  }
  .logo-disc .logo-wordmark { position: absolute; left: 0; width: 100%; top: 226px; font-size: 58px; }

  .overlay-logo { position: absolute; left: 900px; top: 40px; width: 280px; }
  .overlay-logo .brand-circle { width: 84px; height: 84px; margin: 0 auto; border-width: 3px; }
  .overlay-logo .logo-wordmark { font-size: 42px; margin-top: 30px; }

  .phone-screen {
    position: absolute; width: 266px; height: 472px; background: var(--white);
  }
  .board-top .phone-screen { left: 826px; top: 54px; }
  .board-bottom .phone-screen { left: 466px; top: 90px; box-shadow: 0 10px 30px rgba(90,80,70,0.25); }
  .phone-appbar {
    height: 24px; background: var(--brand-blue); display: flex; align-items: center;
    padding: 0 8px; color: var(--white); font-size: 9px; font-weight: 700; gap: 6px;
  }
  .appbar-icon { width: 13px; height: 13px; border-radius: 50%; background: var(--white); }
  .appbar-menu { margin-left: auto; display: flex; flex-direction: column; gap: 2px; }
  .appbar-menu span { width: 3px; height: 3px; border-radius: 50%; background: var(--white); }

  .setpoint-bubble {
    position: absolute; width: 26px; height: 26px; border-radius: 50%;
    border: 1.5px solid var(--brand-blue); color: var(--brand-blue);
    font-size: 11px; font-weight: 500; display: flex; align-items: center; justify-content: center;
  }
  .phone-screen .setpoint-bubble { left: 120px; top: 111px; }
  .phone-screen .dial { position: absolute; left: 45px; top: 153px; width: 176px; height: 176px; }
  .room-name { position: absolute; left: 0; width: 100%; top: 332px; text-align: center; color: var(--brand-blue); font-size: 15px; }
  .room-status { position: absolute; left: 0; width: 100%; top: 351px; text-align: center; color: var(--online-green); font-size: 14px; }

  .watch-screen {
    position: absolute; left: 655px; top: 372px; width: 157px; height: 154px;
    background: var(--white); border: 4px solid var(--brand-blue);
  }
  .watch-screen .dial { position: absolute; left: 33px; top: 33px; width: 84px; height: 84px; }
  .watch-screen .setpoint-bubble { left: 124px; top: 60px; width: 22px; height: 22px; font-size: 9px; }
  .watch-chevron { position: absolute; left: 62px; width: 26px; height: 16px; }
  .watch-chevron.up { top: 6px; }
  .watch-chevron.down { top: 124px; }
</style>
</head>
<body>

<svg width="0" height="0" style="position:absolute">
  <defs>
    <symbol id="thermostat-dial" viewBox="-100 -100 200 200">
      <circle r="98" fill="var(--dial-blue)"/>
      <circle r="86" fill="none" stroke="var(--dial-ring)" stroke-width="14" stroke-dasharray="1 2.2" opacity="0.7"/>
      <circle r="86" fill="none" stroke="var(--heat-red)" stroke-width="16" pathLength="100" stroke-dasharray="38 62" transform="rotate(-82)"/>
      <rect x="-2" y="-96" width="4" height="18" fill="var(--white)" transform="rotate(-8)"/>
      <circle r="74" fill="var(--dial-face)"/>
      <text x="0" y="22" text-anchor="middle" font-family="Roboto, Arial, sans-serif" font-weight="700" font-size="62" fill="var(--digit)">75</text>
      <path d="M-9 -40 L0 -49 L9 -40" fill="none" stroke="var(--digit)" stroke-width="4" stroke-linecap="round" stroke-linejoin="round"/>
      <path d="M-9 42 L0 51 L9 42" fill="none" stroke="var(--digit)" stroke-width="4" stroke-linecap="round" stroke-linejoin="round"/>
    </symbol>
  </defs>
</svg>

<section class="board-top">
  <div class="logo-disc">
    <div class="brand-circle"></div>
    <div class="logo-wordmark">Balmora</div>
  </div>

  <div class="watch-screen">
    <svg class="watch-chevron up" viewBox="0 0 26 16"><path d="M3 13 L13 3 L23 13" fill="none" stroke="var(--brand-blue)" stroke-width="3.5" stroke-linecap="round" stroke-linejoin="round"/></svg>
    <svg class="dial"><use href="#thermostat-dial"/></svg>
    <div class="setpoint-bubble">70</div>
    <svg class="watch-chevron down" viewBox="0 0 26 16"><path d="M3 3 L13 13 L23 3" fill="none" stroke="var(--brand-blue)" stroke-width="3.5" stroke-linecap="round" stroke-linejoin="round"/></svg>
  </div>

  <div class="phone-screen">
    <header class="phone-appbar">
      <span class="appbar-icon"></span>
      <span class="appbar-title">Balmora</span>
      <span class="appbar-menu"><span></span><span></span><span></span></span>
    </header>
    <div class="setpoint-bubble">70</div>
    <svg class="dial"><use href="#thermostat-dial"/></svg>
    <div class="room-name">Living Room</div>
    <div class="room-status">Online</div>
  </div>
</section>

<section class="board-bottom">
  <div class="phone-screen">
    <header class="phone-appbar">
      <span class="appbar-icon"></span>
      <span class="appbar-title">Balmora</span>
      <span class="appbar-menu"><span></span><span></span><span></span></span>
    </header>
    <div class="setpoint-bubble">70</div>
    <svg class="dial"><use href="#thermostat-dial"/></svg>
    <div class="room-name">Living Room</div>
    <div class="room-status">Online</div>
  </div>

  <div class="overlay-logo">
    <div class="brand-circle"></div>
    <div class="logo-wordmark">Balmora</div>
  </div>
</section>

</body>
</html>
```